Etiketten für Brennerei
Wir haben viele kreative Vorschläge für unser neues Etikett erhalten und uns schlussendlich für dieses Design von r2739 entschieden. Bei allen Berwerben und vor allem bei r2739 hat uns gefallen, dass Anmerkungen und Wünsche zum Abändern des Designs direkt umgesetzt wurden. Die Wartezeiten waren sehr kurz und wir können das Portal und diesen Designer nur wärmstens empfehlen.
Zielgruppe
Wir haben eine kleine familiengeführte Brennerei in Karlsruhe (Baden-Württemberg). Wir bieten unseren Kunden vor allem Gin, Whisky und Edeldestillate an. Wir gehen davon aus, dass die Zielgruppe unseres Kieselfink Gins eher kreative, lustige und unkonventionelle Dinge bevorzugt.
Aufgabenstellung
Das Flaschenetikett ist für die Vorderseite eines schwarz gefärbten Gins mit dem Namen Kieselfink. Der Kieselfink sollte in irgendeiner Weise im Design vorkommen. Ansonsten ist es nur wichtig, dass das Design auffällig ist. Es können passende Stockillustrationen oder eigene Illustrationen verwendet werden. Die Flaschenform ist als Bilddatei hinterlegt.

```html
<!DOCTYPE html>
<html lang="de">
<head>
<meta charset="utf-8">
<title>Kieselfink – Black Gin Etikett</title>
<link href="https://fonts.googleapis.com/css2?family=Saira+Condensed:wght@800&family=Great+Vibes&display=swap" rel="stylesheet">
<style>
  :root {
    --backdrop: #000000;
    --label-paper: #ffffff;
    --ink: #111111;
    --accent-orange: #ee6a12;
    --rule: #555555;
  }
  html, body {
    margin: 0;
    padding: 0;
    width: 1200px;
    height: 624px;
    overflow: hidden;
    background: var(--backdrop);
  }
  .canvas {
    position: relative;
    width: 1200px;
    height: 624px;
    background: var(--backdrop);
  }
  .label {
    position: absolute;
    left: 370px;
    top: 32px;
    width: 459px;
    height: 560px;
    background: var(--label-paper);
  }
  .mascot-illustration {
    position: absolute;
    left: 62px;
    top: 67px;
    width: 344px;
    height: 298px;
    display: block;
  }
  .brand-name {
    position: absolute;
    left: 0;
    right: 0;
    top: 394px;
    margin: 0;
    text-align: center;
    font-family: "Saira Condensed", "Arial Narrow", sans-serif;
    font-weight: 800;
    font-size: 80px;
    line-height: 1;
    letter-spacing: 1.5px;
    color: var(--ink);
  }
  .divider {
    position: absolute;
    left: 150px;
    width: 162px;
    top: 484px;
    height: 0;
    border-top: 1px solid var(--rule);
  }
  .product-type {
    position: absolute;
    left: 0;
    right: 0;
    top: 490px;
    margin: 0;
    text-align: center;
    font-family: "Great Vibes", cursive;
    font-size: 31px;
    line-height: 1.2;
    word-spacing: 6px;
    color: var(--ink);
  }
</style>
</head>
<body>
  <main class="canvas">
    <section class="label">
      <svg class="mascot-illustration" role="img" aria-label="Illustration: fröhlich tanzender schwarzer Kieselfink mit ausgebreiteten Flügeln, orangefarbenen Beinen und Wangen, der durch schwarze Pfützen springt" viewBox="0 0 344 298">
        <defs>
          <radialGradient id="mascotTone" cx="50%" cy="46%" r="52%">
            <stop offset="0%" stop-color="#111111"/>
            <stop offset="55%" stop-color="#1c1c1c"/>
            <stop offset="78%" stop-color="#6b4a33"/>
            <stop offset="90%" stop-color="#e9c7ae"/>
            <stop offset="100%" stop-color="#ffffff"/>
          </radialGradient>
        </defs>
        <rect width="344" height="298" fill="url(#mascotTone)"/>
      </svg>
      <h1 class="brand-name">KIESELFINK</h1>
      <div class="divider"></div>
      <p class="product-type">Black Gin</p>
    </section>
  </main>
</body>
</html>
```